Wordpress design for my private practice website - Psychotherapist

I would like a simple, clean, and elegant design for my private practice website. I work with both adults and children so I'd like it to appeal to both. However, since parents make the choice as to where to send their child for therapy, I want it to appeal to adults more. I would like the pictures on the site to have a calming effect - maybe using sand and water and rocks. I am attaching files with my company logo. I would also like my name incorporated into the header - Rosalind Vantreece, LCSW, Registered Play Therapist. I've also uploaded a picture of myself for my About Page.

I like the design of these 2 website and want something similar:
www.drmaribelostrand.com
www.harrowgate-lisk.com

I would like a home page that highlights a calming graphic across the entire top of the page as well as my practice logo and my name.

I'd like a link to social media sites on the top of the homepage - facebook, pinterest.

I want a simple bar across the top with the following tabs:
Home
About Me (subtabs Who I Am, Specialties and Approach)
Counseling Services (subtabs Individual Counseling, Play Therapy, Sandplay Therapy,)
Fees
FAQs
Contact Me (would love this to be a fill in the blank contact form that sends info to my email address - should include name, phone number, email and a comment box for more information requested)
Blog (this will link with another wordpress blog)

Target Market(s)

Parents of children under age 12 with behavioral problems or are dealing with the breakup of their family through divorce - looking for someone to work with their young child. I also work with Adults that are overwhelmed and worried - often women that have many life stressors and are feeling burnt out on life and meeting everyone's needs. Families going through some type of trauma, including divorce or grief work. I also work with individuals going through a transition of religious beliefs - often exiting the religion of their youth and undergoing a crisis of faith at midlife.

Industry/Entity Type

Mental Health

Contact Information for Business Card

Rosalind Vantreece, LCSW
Registered Play Therapist
4815 Bellhaven Court
Idaho Falls, Idaho 83404
(208)555-7162
www.stillbrookwellness.com

On the opposite side, I'd like an appointment reminder area - with the following text:

Your next appointment is
_____/______/______ at ______am/pm
Please give 24 hrs notice if you need to cancel your appointment.

Coding

Coded - Design and coding required

Number of Pages Required

5+ page

Font styles to use
Sans Serif

Colors
33a6d7
9bcb3c
0355a3

Requirements
Must have
• I'd like it to be a wordpress site. I'm such a newby at web design - but I need to be able to add content and manage the site myself once it is up and running.
Nice to have
• I like the design of these 2 websites and want something similar:
• www.drmaribelostrand.com
• www.harrowgate-lisk.com
• They are clean, easy to navigate and calming.
Should not have
• Should not look like a childcare website.

```html
<!DOCTYPE html>
<html lang="en">
<head>
<meta charset="utf-8">
<title>Dr. Maribel Ostrand — Stillbrook Wellness</title>
<link href="https://fonts.googleapis.com/css2?family=Oswald:wght@400;500&family=Lato:wght@400;700&family=Roboto+Slab:wght@500&display=swap" rel="stylesheet">
<style>
:root{
  --blue-deep:#0355a3;
  --blue-sky:#33a6d7;
  --green-leaf:#9bcb3c;
  --ink:#222;
  --muted:#8a8a8a;
  --white:#fff;
  --tile-text:#f2f2f2;
}
*{box-sizing:border-box;margin:0;padding:0}
html,body{width:1200px;height:2247px;overflow:hidden}
body{position:relative;background:var(--white);font-family:"Lato",Arial,sans-serif;color:var(--ink)}
.abs{position:absolute}

/* header */
.hero{left:0;top:0;width:1200px;height:345px;background:radial-gradient(ellipse at 30% 40%,#eef0ec 0,#b9c2b4 22%,#3d4a35 55%,#1f2a1c 100%)}
.nav-band{left:0;top:0;width:1200px;height:21px;background:var(--blue-deep)}
.brand{left:249px;top:0;width:168px;height:84px;background:var(--white);display:flex;flex-direction:column;align-items:center;justify-content:center;gap:4px}
.brand-dot{width:18px;height:18px;border-radius:50%;background:var(--blue-deep)}
.brand-name{font-size:14px;letter-spacing:2px;color:var(--blue-deep);font-weight:400;text-transform:uppercase}
.nav{top:0;height:21px;display:flex;align-items:center;font-size:9.5px;font-weight:700;color:var(--white);text-transform:uppercase;letter-spacing:.5px}
.nav.active{color:var(--green-leaf);text-decoration:underline}
.nav-blog{left:900px;top:0;width:48px;height:21px;background:var(--green-leaf);color:var(--white);font-size:9px;font-weight:700;display:flex;align-items:center;justify-content:center}
.submenu{background:var(--blue-deep);border:1px solid var(--blue-sky);font-size:7px;color:var(--white)}
.submenu div{height:14px;line-height:14px;text-align:center;border-bottom:1px solid var(--blue-sky)}
.submenu .sel{color:var(--green-leaf)}
.hero-name{left:267px;top:142px;width:289px;height:50px;background:rgba(155,203,60,.85);font-family:"Roboto Slab",Georgia,serif;font-size:32px;color:#2f3a2a;padding-left:12px;line-height:50px}
.hero-intro{left:267px;top:195px;width:426px;height:82px;background:rgba(51,166,215,.85);color:var(--white);font-size:11.5px;line-height:15px;padding:16px 12px}
.dots{left:570px;top:315px;display:flex;gap:4px}
.dots span{width:9px;height:9px;border-radius:50%;border:1.5px solid var(--white)}
.dots .on{background:var(--white)}

/* sections */
.section-title{font-family:"Oswald",Arial,sans-serif;font-size:24px;color:var(--blue-deep);text-transform:uppercase;line-height:1}
.btn{background:var(--blue-sky);color:var(--white);font-size:13px;display:flex;align-items:center;justify-content:center;box-shadow:0 3px 0 #1d6f93}
.about-name{left:253px;top:420px;font-size:13px;color:var(--blue-deep)}
.about-text{left:253px;top:442px;width:570px;font-size:8.5px;line-height:12px;color:var(--muted)}
.portrait{left:835px;top:388px;width:111px;height:149px;background:linear-gradient(160deg,#d9c48a,#9a8a5a 60%,#5c6b3a);border:2px solid #e4d7a8}

.grid{left:253px;top:652px;width:695px;height:393px;display:grid;grid-template-columns:repeat(3,1fr);gap:3px}
.tile{position:relative;color:var(--tile-text);text-align:center;padding:26px 14px 0}
.tile h3{font-size:17px;color:var(--blue-sky);font-weight:700;margin-bottom:10px}
.tile p{font-size:10.5px;line-height:13px}
.tile .btn{position:absolute;left:50%;transform:translateX(-50%);bottom:16px;width:128px;height:20px;font-size:12px}
.t1{background:linear-gradient(135deg,#5b5148,#2f2a26)}
.t2{background:linear-gradient(135deg,#4b3a2e,#231b16)}
.t3{background:linear-gradient(135deg,#55575a,#2d2f31)}
.t4{background:linear-gradient(135deg,#4d4943,#2a2724)}
.t5{background:linear-gradient(135deg,#5a3a22,#1e140d)}
.t6{background:linear-gradient(135deg,#5e5e5e,#393939)}

.card{top:1124px;height:301px;border:1px solid var(--blue-sky);background:#f3f3f3;text-align:center}
.card-photo{height:160px}
.card-icon{position:absolute;left:50%;top:145px;transform:translateX(-50%);width:34px;height:34px;border-radius:50%;background:var(--blue-sky);display:flex;align-items:center;justify-content:center}
.card h3{margin-top:32px;font-size:15px;font-weight:400}
.card p{margin:8px auto 0;width:150px;font-size:9px;line-height:11px;color:#666}
.card .btn{position:absolute;left:50%;transform:translateX(-50%);bottom:18px;width:128px;height:21px}

.post-title{left:254px;top:1520px;font-size:13px;font-weight:700;color:var(--blue-deep);letter-spacing:.3px}
.post-photo{left:253px;top:1543px;width:522px;height:189px;background:linear-gradient(90deg,#1d3b3f,#2f5a5a 30%,#4a2b2f 65%,#3a2a26)}
.archive{left:791px;top:1543px;width:156px;height:189px;background:var(--blue-sky);color:var(--blue-deep);text-align:center;font-size:10px}
.archive h4{color:var(--white);font-size:11px;font-weight:700;padding:7px 0 6px}
.archive li{list-style:none;height:15.8px;line-height:15.8px;border-top:1px solid rgba(255,255,255,.45)}
.excerpt{left:253px;top:1742px;width:460px;font-size:8.5px;line-height:12px;color:var(--muted)}
.post-date{left:256px;top:1774px;font-size:8.5px;color:var(--blue-deep);font-weight:700;display:flex;gap:5px;align-items:center}
.post-actions{left:257px;top:1798px;display:flex;gap:8px}

/* footer */
.footer{left:0;top:1885px;width:1200px;height:319px;background:var(--blue-deep)}
.foot-title{font-size:22px;color:var(--white);font-weight:400;text-transform:uppercase;letter-spacing:.5px}
.field{background:var(--white);font-size:8px;color:#999;padding:8px 7px;text-transform:uppercase;letter-spacing:.5px}
.submit{left:249px;top:2083px;width:127px;height:21px;background:var(--blue-sky);color:var(--white);font-size:14px;display:flex;align-items:center;justify-content:center;box-shadow:0 3px 0 #0a3b6d;letter-spacing:1px}
.signup-note{left:748px;top:1935px;width:220px;font-size:15px;line-height:18px;color:var(--green-leaf)}
.email-field{left:748px;top:1975px;width:135px;height:17px;background:#053f7a;border:1px solid #2b6cb0;font-size:7px;color:#8aa9cc;padding:4px}
.signup-btn{left:887px;top:1975px;width:48px;height:17px;background:var(--green-leaf);color:var(--white);font-size:8px;font-weight:700;display:flex;align-items:center;justify-content:center}
.info{top:2134px;width:168px;height:39px;display:flex;color:var(--white)}
.info-icon{width:34px;background:#0a4a8c;display:flex;align-items:center;justify-content:center}
.info-body{flex:1;background:#0f5fae;padding:6px 10px 0 14px}
.info-body b{display:block;font-size:8px;font-weight:400;text-transform:uppercase}
.info-body span{display:block;font-size:6.5px;line-height:8px;margin-top:2px}
.bottom-bar{left:0;top:2204px;width:1200px;height:43px;background:var(--blue-sky)}
.copyright{left:251px;top:2219px;font-size:11px;color:var(--white)}
.social{left:852px;top:2219px;display:flex;gap:9px}
.social span{width:12px;height:12px;border-radius:50%;background:var(--white)}
</style>
</head>
<body>

<header>
  <div class="abs hero" role="img" aria-label="Photo of white snowdrop flowers against a soft dark background"></div>
  <div class="abs nav-band"></div>
  <div class="abs brand"><span class="brand-dot"></span><span class="brand-name">Stillbrook Wellness</span></div>
  <nav>
    <a class="abs nav active" style="left:438px">Home</a>
    <a class="abs nav" style="left:489px">About Me</a>
    <a class="abs nav" style="left:565px">Counseling Services</a>
    <a class="abs nav" style="left:697px">Fees</a>
    <a class="abs nav" style="left:745px">FAQs</a>
    <a class="abs nav" style="left:792px">Contact Me</a>
    <a class="abs nav-blog">BLOG</a>
    <div class="abs submenu" style="left:469px;top:24px;width:86px"><div class="sel">Suitable Who I Am</div><div>Specialties and Approach</div></div>
    <div class="abs submenu" style="left:565px;top:24px;width:102px"><div>Suitable Individual Counseling</div><div>Play Therapy</div><div class="sel">Sandplay Therapy</div></div>
  </nav>
  <h1 class="abs hero-name">Dr.Maribel Ostrand</h1>
  <p class="abs hero-intro">Dr. Maribel Ostrand is a licensed psychologist specializing in relationships, infertility counseling, and sexuality. She has taught college-level courses on psychological wellness and healthy relationships, led psychotherapy groups on coping with anxiety and depression.</p>
  <div class="abs dots"><span class="on"></span><span></span><span></span><span></span></div>
</header>

<section class="about">
  <h2 class="abs section-title" style="left:249px;top:384px">About Me</h2>
  <p class="abs about-name">Dr. Helena Harrowgate-Lisk</p>
  <p class="abs about-text">I am a licensed psychotherapist with a PhD in Counseling Psychology from Westbrook University. I wrote my dissertation on LDS women and sexuality, have taught college-level courses on human sexuality, and currently teach online and community-based relationship and sexuality courses to LDS couples. I am a frequent contributor on the subjects of sexuality, mental health and spirituality to LDS-themed blogs, magazines, and podcasts.</p>
  <a class="abs btn" style="left:253px;top:511px;width:153px;height:24px">Read More</a>
  <div class="abs portrait" role="img" aria-label="Portrait photo of the therapist"></div>
</section>

<section class="specialties">
  <h2 class="abs section-title" style="left:249px;top:598px">Specialties and Approach</h2>
  <div class="abs grid">
    <article class="tile t1" role="img" aria-label="Relationship counseling photo background"><h3>Relationship Counseling</h3><p>Do you long to feel more loved and appreciated by your partner? Are you tired of the unproductive fights? Is the unhappiness causing the two of you to drift apart?</p><a class="btn">Read More</a></article>
    <article class="tile t2" role="img" aria-label="Sexuality photo background"><h3>Sexuality</h3><p>Almost all couples deal with sexual issues at some point in the course of long-term relationships. Because sexual problems affect how.....</p><a class="btn">Read More</a></article>
    <article class="tile t3" role="img" aria-label="Depression photo background"><h3>Depression</h3><p>The National Wellness Research Council estimates that approximately 17 million American adults suffer from depression each year.</p><a class="btn">Read More</a></article>
    <article class="tile t4" role="img" aria-label="Women's issues photo background"><h3>Women's Issues</h3><p>I have a particular passion for helping women. I studied women's studies as an undergraduate and feminist-relational models of therapy in graduate school.</p><a class="btn">Read More</a></article>
    <article class="tile t5" role="img" aria-label="Spirituality and identity photo background"><h3>Spirituality &amp; Identity</h3><p>Spirituality is about finding an inner compass that guides you and gives you strength. Identifying and trusting this source of wisdom is an important part of</p><a class="btn">Read More</a></article>
    <article class="tile t6" role="img" aria-label="Parenting photo background"><h3>Parenting</h3><p>Do you have a difficult teenager or young child? Do you feel unclear about how and where to set limits, or how to respond to disobedience?</p><a class="btn">Read More</a></article>
  </div>
</section>

<section class="services">
  <h2 class="abs section-title" style="left:249px;top:1080px">Counseling Services</h2>
  <article class="abs card" style="left:258px;width:214px">
    <div class="card-photo" role="img" aria-label="Photo of a counseling session on a white sofa" style="background:linear-gradient(135deg,#d8d4cc,#8e8478)"></div>
    <span class="card-icon"><svg width="16" height="16" viewBox="0 0 16 16" fill="none" stroke="#fff" stroke-width="2"><rect x="1" y="6" width="8" height="4" rx="2" transform="rotate(-45 5 8)"/><rect x="7" y="6" width="8" height="4" rx="2" transform="rotate(-45 11 8)"/></svg></span>
    <h3>Individual Counseling</h3><p>Lorem Ipsum is simply dummy text of the printing and typesetting industry.</p><a class="btn">Read More</a>
  </article>
  <article class="abs card" style="left:486px;width:219px">
    <div class="card-photo" role="img" aria-label="Photo of a play therapy session with a board game" style="background:linear-gradient(135deg,#b7ad9f,#6f8a4a)"></div>
    <span class="card-icon"><svg width="16" height="16" viewBox="0 0 16 16" fill="none" stroke="#fff" stroke-width="2"><rect x="1" y="6" width="8" height="4" rx="2" transform="rotate(-45 5 8)"/><rect x="7" y="6" width="8" height="4" rx="2" transform="rotate(-45 11 8)"/></svg></span>
    <h3>Play Therapy</h3><p>Lorem Ipsum is simply dummy text of the printing and typesetting industry.</p><a class="btn">Read More</a>
  </article>
  <article class="abs card" style="left:718px;width:225px">
    <div class="card-photo" role="img" aria-label="Photo of a couple seated on a sofa in session" style="background:linear-gradient(135deg,#e0ddd6,#7f8fa2)"></div>
    <span class="card-icon"><svg width="16" height="16" viewBox="0 0 16 16" fill="none" stroke="#fff" stroke-width="2"><rect x="1" y="6" width="8" height="4" rx="2" transform="rotate(-45 5 8)"/><rect x="7" y="6" width="8" height="4" rx="2" transform="rotate(-45 11 8)"/></svg></span>
    <h3>Sandplay Therapy</h3><p>Lorem Ipsum is simply dummy text of the printing and typesetting industry.</p><a class="btn">Read More</a>
  </article>
</section>

<section class="blog">
  <h2 class="abs section-title" style="left:249px;top:1466px">Blog</h2>
  <h3 class="abs post-title">A Review of The Craft of Closeness course by Hearth &amp; Home Blogger</h3>
  <div class="abs post-photo" role="img" aria-label="Photo of a couple holding hands above scattered fruit"></div>
  <aside class="abs archive">
    <h4>BLOG LIST</h4>
    <ul><li>February 2016</li><li>December 2015</li><li>November 2015</li><li>October 2015</li><li>September 2015</li><li>July 2015</li><li>May 2015</li><li>April 2015</li><li>March 2015</li><li>February 2015</li></ul>
  </aside>
  <p class="abs excerpt">Marisol, writing for weblog "Two Hearts Journal" reviews my online course in a post titled Resources for Improving Intimacy: "The Craft of Closeness"</p>
  <p class="abs post-date"><svg width="9" height="9" viewBox="0 0 10 10" fill="none" stroke="#0355a3" stroke-width="1.4"><circle cx="5" cy="5" r="4"/><path d="M5 2.5V5l2 1"/></svg>24 Feb 2016</p>
  <div class="abs post-actions">
    <svg width="10" height="9" viewBox="0 0 10 9"><path d="M1 1h8v5H4L2 8V6H1z" fill="#0355a3"/></svg>
    <svg width="10" height="9" viewBox="0 0 10 9"><path d="M5 8.5L1 4.5A2.2 2.2 0 0 1 5 2a2.2 2.2 0 0 1 4 2.5z" fill="#0355a3"/></svg>
    <svg width="9" height="9" viewBox="0 0 10 10" fill="#0355a3"><circle cx="8" cy="2" r="1.6"/><circle cx="2" cy="5" r="1.6"/><circle cx="8" cy="8" r="1.6"/><path d="M8 2L2 5l6 3" stroke="#0355a3" fill="none"/></svg>
  </div>
  <a class="abs btn" style="left:253px;top:1820px;width:129px;height:21px">Read More</a>
</section>

<footer>
  <div class="abs footer"></div>
  <h2 class="abs foot-title" style="left:249px;top:1898px">Contact Us</h2>
  <div class="abs field" style="left:249px;top:1936px;width:196px;height:27px">Name:</div>
  <div class="abs field" style="left:449px;top:1936px;width:197px;height:27px">Email:</div>
  <div class="abs field" style="left:249px;top:1975px;width:397px;height:27px">Subject</div>
  <div class="abs field" style="left:249px;top:2012px;width:397px;height:56px">Message:</div>
  <a class="abs submit">SUBMIT</a>

  <h2 class="abs foot-title" style="left:748px;top:1902px">Sign Up</h2>
  <p class="abs signup-note">Sign up with your email address to receive news and updates!</p>
  <div class="abs email-field">Enter Email</div>
  <a class="abs signup-btn">SIGN UP</a>

  <div class="abs info" style="left:249px"><span class="info-icon"><svg width="10" height="13" viewBox="0 0 10 13"><path d="M5 12S1 7 1 4.5a4 4 0 0 1 8 0C9 7 5 12 5 12z" fill="#fff"/><circle cx="5" cy="4.5" r="1.5" fill="#0a4a8c"/></svg></span><div class="info-body"><b>Office Address</b><span>318 Alder Lane, Maple Ridge, GA 30699, United States</span></div></div>
  <div class="abs info" style="left:515px"><span class="info-icon"><svg width="11" height="11" viewBox="0 0 12 12"><path d="M3 1l2 3-1.3 1.3a7 7 0 0 0 3 3L8 7l3 2-1 2C5 11 1 7 1 2z" fill="#fff"/></svg></span><div class="info-body"><b>Phone Address</b><span>847-555-0193</span></div></div>
  <div class="abs info" style="left:782px"><span class="info-icon"><svg width="12" height="9" viewBox="0 0 12 9" fill="none" stroke="#fff" stroke-width="1.3"><rect x=".7" y=".7" width="10.6" height="7.6"/><path d="M.7.7L6 5l5.3-4.3"/></svg></span><div class="info-body"><b>Email Address</b><span>helena@harrowgate-lisk.com</span></div></div>

  <div class="abs bottom-bar"></div>
  <p class="abs copyright">© 2016 Maribel Ostrand. All rights reserved</p>
  <div class="abs social" aria-label="Social links"><span></span><span></span><span></span><span></span></div>
</footer>

</body>
</html>
```